business card design and letterhead for a building inspection company. We have a pre-purchase building and pest inspection ( i inspect house before people purchase it)
Updates

Linda has been so so responsive and good, i highly recommend her

Industry/Entity Type

Building

Contact Information for Business Card

audience, solicitor, real estate agent, mortgage brokerthe rest of the info will be in the attachement business card

```html
<!DOCTYPE html>
<html lang="en">
<head>
<meta charset="utf-8">
<title>Keystone Property Inspections – Business Card</title>
<link href="https://fonts.googleapis.com/css2?family=Noto+Sans:wght@400;600&display=swap" rel="stylesheet">
<style>
  :root {
    --brand-blue: #0b72bd;
    --icon-blue: #1677c4;
    --paper: #ffffff;
    --edge: #1c1c1c;
    --page: #ffffff;
  }
  * { box-sizing: border-box; margin: 0; padding: 0; }
  html, body {
    width: 855px; height: 1200px; overflow: hidden;
    background: var(--page);
    font-family: "Noto Sans", Verdana, sans-serif;
  }
  .canvas { position: relative; width: 855px; height: 1200px; }

  .card {
    position: absolute; left: 67px; width: 720px; height: 443px;
    background: var(--brand-blue); overflow: hidden;
  }
  .card--front { top: 55px; }
  .card--back { top: 660px; border: 2px solid var(--edge); }

  /* front */
  .logo-tab {
    position: absolute; left: 190px; top: 0; width: 351px; height: 309px;
    background: var(--paper); border-radius: 0 0 40px 40px;
    display: flex; align-items: center; justify-content: center;
    padding-top: 90px;
  }
  .website {
    position: absolute; left: 0; right: 0; top: 352px;
    text-align: center; color: var(--paper); font-size: 31px; letter-spacing: 0.3px;
  }

  /* brand name stand-in */
  .brand { display: flex; align-items: center; gap: 12px; color: var(--brand-blue); font-weight: 600; }
  .brand__mark { width: 30px; height: 30px; background: var(--brand-blue); flex: none; }
  .brand__name { line-height: 1.1; }
  .brand__name span { display: block; }
  .brand--front .brand__name { font-size: 26px; }
  .brand--front .brand__name span + span { font-size: 15px; }
  .brand--back .brand__name { font-size: 24px; }
  .brand--back .brand__name span + span { font-size: 14px; }

  /* back */
  .logo-panel {
    position: absolute; left: 404px; top: 18px; width: 286px; height: 106px;
    background: var(--paper);
    display: flex; align-items: center; justify-content: center;
  }
  .contact-list {
    position: absolute; right: 82px; top: 180px;
    list-style: none; text-align: right; color: var(--paper); font-size: 30px;
  }
  .contact-list li { height: 57px; line-height: 44px; }
  .icon-tab {
    position: absolute; right: -2px; top: 163px; width: 70px; height: 184px;
    background: var(--paper); border-radius: 9px 0 0 9px;
    display: flex; flex-direction: column; align-items: center; justify-content: space-around;
    padding: 10px 0;
  }
  .icon-tab svg { width: 30px; height: 34px; fill: var(--icon-blue); }
  .audience {
    position: absolute; left: 0; right: 0; top: 380px;
    text-align: center; color: var(--paper); font-size: 30px;
  }
</style>
</head>
<body>
<main class="canvas">

  <section class="card card--front">
    <div class="logo-tab">
      <div class="brand brand--front">
        <div class="brand__mark"></div>
        <div class="brand__name"><span>KEYSTONE</span><span>PROPERTY INSPECTIONS</span></div>
      </div>
    </div>
    <p class="website">www.keystoneinspect.com.au</p>
  </section>

  <section class="card card--back">
    <div class="logo-panel">
      <div class="brand brand--back">
        <div class="brand__mark"></div>
        <div class="brand__name"><span>KEYSTONE</span><span>PROPERTY INSPECTIONS</span></div>
      </div>
    </div>

    <ul class="contact-list">
      <li class="contact-list__phone">029000 1234</li>
      <li class="contact-list__mobile">0400 000 111</li>
      <li class="contact-list__email">info@keystoneinspect.com.au</li>
    </ul>

    <div class="icon-tab">
      <svg viewBox="0 0 24 24" aria-label="Phone"><path d="M6.6 2.5c.6-.3 1.3 0 1.6.6l1.6 3.4c.3.6.1 1.2-.4 1.6l-1.5 1.1c.9 2.3 2.3 4.3 4.1 5.9l1.4-1.2c.5-.4 1.2-.4 1.7 0l3 2.3c.5.4.6 1.1.3 1.7l-1.2 2c-.5.8-1.5 1.2-2.4.9C8.4 19.3 4.3 13.7 3.6 6.9c-.1-1 .4-1.9 1.3-2.4z"/></svg>
      <svg viewBox="0 0 24 24" aria-label="Mobile"><path d="M9 1h1.5v3H16a2 2 0 0 1 2 2v15a2 2 0 0 1-2 2H8a2 2 0 0 1-2-2V6a2 2 0 0 1 2-2h1zM8.5 7v5h7V7zm0 7v1.5h2V14zm3 0v1.5h2V14zm3 0v1.5h1V14zm-6 3v1.5h2V17zm3 0v1.5h2V17zm3 0v1.5h1V17z"/></svg>
      <svg viewBox="0 0 24 24" aria-label="Email"><path d="M2 5h20v14H2zm1.8 1.5L12 13l8.2-6.5zM3.5 8v9.5h17V8L12 15z"/></svg>
    </div>

    <p class="audience">Audience, Solicitor, Real Estate Agent</p>
  </section>

</main>
</body>
</html>
```